Dental practice logo either "Dental Lumora Centre" or "Dental Lumora Centre"

Dental practice with either of the logos mentioned above as we haven't decided on the name depends on which one looks better. Our motto of the practice is to create beautiful smiles and perform general dentistry.
Dr Suresh Nandakumar
47 Wattlebrook Road
Deeragun
Queensland 4814 and also the contact number, email address and website.
On the backside of the card it should be about the next appointment and also mention on the bottom" If unable to keep an appointment kindly give 24 hours notice otherwise a fee will be charged for the time reserved.
Reason: As it may take longer to design
We want the business card only on the dental practice named Dental Lumora Centre and with a caption underneath the practice name as "Townsville's home of dentistry"
Target Market(s)
dental patients and general population who want beautiful smile
Industry/Entity Type
Dental

```html
<!DOCTYPE html>
<html lang="en">
<head>
<meta charset="UTF-8">
<title>Dental Lumora Centre – Business Card</title>
<link rel="stylesheet" href="https://fonts.googleapis.com/css2?family=Open+Sans:wght@300;400;600;700&display=swap">
<style>
  :root {
    --bg-top: #f4f4f4;
    --bg-bottom: #d9d9d9;
    --card: #fbfbfb;
    --ink: #2b2b2b;
    --ink-soft: #555555;
    --rule: #c9c9c9;
    --band-dark: #1f1d1e;
    --warm-red: #ee4136;
    --warm-orange: #f7a42a;
    --on-dark: #ffffff;
  }
  * { box-sizing: border-box; margin: 0; padding: 0; }
  html, body { width: 1200px; height: 883px; overflow: hidden; }
  body {
    font-family: "Open Sans", sans-serif;
    background: linear-gradient(160deg, var(--bg-top), var(--bg-bottom));
    position: relative;
    color: var(--ink);
  }
  .card {
    position: absolute;
    width: 560px;
    height: 320px;
    background: var(--card);
    border-radius: 26px;
    overflow: hidden;
    box-shadow: 0 12px 30px rgba(0,0,0,0.16);
  }

  /* Back face */
  .card-back { left: 590px; top: 70px; }
  .brand {
    position: absolute;
    left: 44px; top: 82px;
    display: flex; align-items: center; gap: 12px;
  }
  .brand-dot {
    width: 38px; height: 38px; border-radius: 50%;
    background: var(--warm-red);
    flex-shrink: 0;
  }
  .brand-name {
    font-weight: 600;
    font-size: 19px;
    line-height: 1.1;
    letter-spacing: 0.5px;
    color: var(--ink);
    text-transform: uppercase;
  }
  .brand-caption {
    position: absolute;
    left: 94px; top: 136px;
    font-size: 11px;
    font-style: normal;
    color: var(--ink-soft);
    letter-spacing: 0.3px;
  }
  .web-strip {
    position: absolute;
    left: 316px; top: 70px;
    width: 244px; height: 62px;
    display: flex;
  }
  .web-strip-label {
    flex: 1;
    background: var(--band-dark);
    color: var(--on-dark);
    font-size: 9px;
    letter-spacing: 1.2px;
    display: flex; align-items: center; justify-content: center;
  }
  .web-strip-accent {
    width: 60px;
    background: radial-gradient(circle at 40% 50%, var(--warm-orange), var(--warm-red) 80%);
  }
  .appointment {
    position: absolute;
    left: 44px; right: 44px; top: 176px;
  }
  .appointment-title {
    font-size: 12px;
    font-weight: 700;
    text-transform: uppercase;
    letter-spacing: 1px;
    margin-bottom: 8px;
  }
  .appointment-row {
    display: flex; gap: 14px;
    font-size: 11px;
    color: var(--ink-soft);
    text-transform: uppercase;
  }
  .appointment-field {
    flex: 1;
    border-bottom: 1px solid var(--rule);
    padding-bottom: 14px;
  }
  .appointment-note {
    position: absolute;
    left: 44px; right: 44px; bottom: 20px;
    font-size: 9.5px;
    line-height: 1.4;
    color: var(--ink-soft);
    text-align: center;
  }

  /* Front face */
  .card-front { left: 60px; top: 480px; }
  .holder {
    position: absolute;
    top: 38px; left: 0; right: 0;
    text-align: center;
  }
  .holder-name {
    font-size: 25px;
    font-weight: 300;
    letter-spacing: 0.5px;
    text-transform: uppercase;
  }
  .holder-name strong { font-weight: 700; }
  .holder-role {
    font-size: 12px;
    font-weight: 400;
    color: var(--ink-soft);
    text-transform: uppercase;
    margin-top: 2px;
  }
  .holder-role strong { font-weight: 700; }
  .contact-band {
    position: absolute;
    left: 0; right: 0; top: 120px; height: 96px;
    display: flex;
  }
  .band-edge { width: 18px; background: var(--band-dark); }
  .band-phone {
    width: 270px;
    background: linear-gradient(100deg, var(--warm-red) 20%, var(--warm-orange));
    color: var(--on-dark);
    padding: 16px 0 0 66px;
    font-size: 15px;
    line-height: 1.3;
  }
  .band-web {
    flex: 1;
    background: var(--band-dark);
    color: var(--on-dark);
    text-align: center;
    padding-top: 16px;
    font-size: 14px;
    line-height: 1.3;
    text-transform: uppercase;
  }
  .band-heading { text-transform: uppercase; }
  .address {
    position: absolute;
    left: 0; right: 0; top: 236px;
    text-align: center;
    font-size: 13px;
    line-height: 1.4;
    text-transform: uppercase;
    color: var(--ink);
  }
  .address strong { font-weight: 700; }
</style>
</head>
<body>
  <section class="card card-back" aria-label="Business card back">
    <div class="brand">
      <span class="brand-dot"></span>
      <span class="brand-name">Dental Lumora<br>Centre</span>
    </div>
    <p class="brand-caption">Townsville's home of dentistry</p>
    <div class="web-strip">
      <div class="web-strip-label">WWW.LUMORADENTAL.COM</div>
      <div class="web-strip-accent"></div>
    </div>
    <div class="appointment">
      <p class="appointment-title">Your next appointment</p>
      <div class="appointment-row">
        <span class="appointment-field">Date</span>
        <span class="appointment-field">Time</span>
      </div>
    </div>
    <p class="appointment-note">If unable to keep an appointment kindly give 24 hours notice otherwise a fee will be charged for the time reserved.</p>
  </section>

  <section class="card card-front" aria-label="Business card front">
    <div class="holder">
      <h1 class="holder-name">Dr Suresh <strong>Nandakumar</strong></h1>
      <p class="holder-role"><strong>Beautiful smiles</strong> &amp; general dentistry</p>
    </div>
    <div class="contact-band">
      <div class="band-edge"></div>
      <div class="band-phone">
        <p class="band-heading">Phone &amp; Fax</p>
        <p>07 4700 1523</p>
        <p>07 4700 1524</p>
      </div>
      <div class="band-web">
        <p class="band-heading">Email &amp; Web</p>
        <p>care@lumoradental.com</p>
        <p>www.lumoradental.com</p>
      </div>
    </div>
    <p class="address">47 <strong>Wattlebrook</strong> Road, Deeragun<br><strong>Queensland 4814</strong></p>
  </section>
</body>
</html>
```